nutrition ebook cover

i need a cover for a ebook designed, the book is called Amber Lattice so i would like that somewhere on the cover. i would also like the word nutrition followed by my company logo that i have attached below somewhere on the cover( i have attached two logos and would like to see with both separatley), i would like this to be faded into the background if possible, perhaps in a upper or lower corner. i would also like to see options with and without the picture i have attached below. the look I'm going for is professional and clean. this is a fat loss, healthy eating booklet. the winning designer i would like to design the following pages within the book aswell no more than 10 pages, that i will provide all content for, i just need help with putting what i have on pdf in a way that looks professional and cool. this would ideally covered in the rate that is paid for the cover. i also have other booklets i need made so the winning designer will most likely get that work too at a later date for an additional fee of course.

Industry/Entity Type

Nutrition

Requirements
Nice to have
• Outside images are welcomed, happy to purchase any stock images used from a outside source

```html
<!DOCTYPE html>
<html lang="en">
<head>
<meta charset="utf-8">
<title>Amber Lattice — nutrition ebook cover</title>
<link href="https://fonts.googleapis.com/css2?family=Lato:wght@100;300;400&display=swap" rel="stylesheet">
<style>
  :root {
    --cover-dark: #231f20;
    --ink-white: #f4f2ef;
    --accent-red: #c0272d;
    --title-ink: #1c1613;
    --wood-light: #a8683c;
    --wood-deep: #6e3d1f;
    --slate: #2c3a3c;
    --slate-deep: #1a2324;
  }
  * { margin: 0; padding: 0; box-sizing: border-box; }
  html, body {
    width: 901px; height: 1200px; overflow: hidden;
    background: var(--cover-dark);
  }
  .cover {
    position: relative;
    width: 901px; height: 1200px;
    background: var(--cover-dark);
    font-family: "Lato", sans-serif;
  }
  .hero-photo {
    position: absolute;
    left: 0; top: 240px;
    width: 901px; height: 690px;
    background:
      radial-gradient(ellipse 260px 300px at 50% 52%, var(--wood-light) 0%, var(--wood-deep) 70%, transparent 100%),
      radial-gradient(ellipse at 50% 50%, var(--slate) 0%, var(--slate-deep) 100%);
  }
  .book-title {
    position: absolute;
    left: 0; top: 520px;
    width: 901px;
    text-align: center;
    color: var(--title-ink);
  }
  .book-title__main {
    display: block;
    font-weight: 100;
    font-size: 118px;
    line-height: 1;
    letter-spacing: 2px;
  }
  .book-title__sub {
    display: inline-block;
    margin-top: 10px;
    padding: 2px 24px 8px;
    border: 2px solid var(--title-ink);
    font-weight: 100;
    font-size: 52px;
    line-height: 1.1;
  }
  .brand {
    position: absolute;
    right: 48px; top: 150px;
    display: flex; align-items: center; gap: 14px;
    color: var(--ink-white);
    font-weight: 300;
    font-size: 30px;
    letter-spacing: 3px;
  }
  .brand__dot {
    width: 26px; height: 26px;
    border-radius: 50%;
    background: var(--ink-white);
  }
  .tagline {
    position: absolute;
    left: 0; top: 976px;
    width: 901px;
    display: flex; justify-content: center; align-items: center;
    color: var(--ink-white);
    font-weight: 300;
    font-size: 36px;
    letter-spacing: 9px;
  }
  .tagline__divider {
    display: inline-block;
    width: 2px; height: 42px;
    margin: 0 10px 0 4px;
    background: var(--accent-red);
  }
</style>
</head>
<body>
  <main class="cover">
    <div class="brand">
      <span class="brand__dot"></span>
      <span class="brand__name">Halden Fitness</span>
    </div>

    <div class="hero-photo" role="img" aria-label="Overhead photo of a wooden cutting board on dark slate, surrounded by fresh vegetables: potatoes, broccoli, carrot, mushrooms, cherry tomatoes, spring onion, lemon and chilli"></div>

    <h1 class="book-title">
      <span class="book-title__main">Amber</span>
      <span class="book-title__sub">Lattice</span>
    </h1>

    <p class="tagline">
      <span>nutrition</span><span class="tagline__divider"></span><span>health</span><span class="tagline__divider"></span><span>life</span>
    </p>
  </main>
</body>
</html>
```